Courier company needs a Facebook page

Swift Lantern Courier & Delivery Services is a new company and I need a Facebook page. We will be handling small deliveries up to 20 pounds. We aim to have 70 percent of our business from commercial clients and 30 percent from residential clients. We promise 100 % customer satisfaction and offer our services 24 hours a day 7 days a week 365 days a year . We will only be delivering within Yellowknife, NWT , Canada. Our tag line is On Time Every Time.

Target Market(s)

Professional types

Industry/Entity Type

Residential

Requirements
Must have
• My facebook page is blank so I need all the areas covered. The large banner picture should really catch my eye and convey speed of delivery or perhaps a skyline view of Yellowknife, NWT, Canada. Another possibility is to show the spectacular northern lights that Yellowknife is famous for.
Nice to have
• I would probably like a stunning picture that has something to do with delivering for the large area and perhaps my logo in the smaller picture.

```html
<!DOCTYPE html>
<html lang="en">
<head>
<meta charset="utf-8">
<title>Swift Lantern Courier &amp; Delivery Services – Facebook Cover</title>
<link rel="stylesheet" href="https://fonts.googleapis.com/css2?family=Anton&family=Open+Sans:wght@400;600&family=Roboto:ital,wght@0,700;1,700;1,900&display=swap">
<style>
  :root {
    --stage-top: #6a6a6a;
    --stage-bottom: #3c3c3c;
    --cover-bg: #000000;
    --headline-red: #ef4b55;
    --headline-green: #8cc63f;
    --accent-yellow: #f4ea2a;
    --text-white: #ffffff;
    --text-black: #111111;
    --profile-bg: #f5f7f6;
    --brand-blue: #1e4fa0;
    --skyline-top: #5a4540;
    --skyline-bottom: #2a1e1b;
  }
  * { margin: 0; padding: 0; box-sizing: border-box; }
  html, body { width: 1200px; height: 999px; overflow: hidden; }
  body {
    position: relative;
    background: radial-gradient(ellipse at 50% 40%, var(--stage-top), var(--stage-bottom));
    font-family: "Open Sans", Arial, sans-serif;
  }
  .cover {
    position: absolute; left: 26px; top: 270px;
    width: 1146px; height: 424px;
    background: var(--cover-bg);
    overflow: hidden;
  }
  .headline {
    position: absolute;
    font-family: "Anton", Impact, sans-serif;
    font-size: 92px; line-height: 1;
    letter-spacing: 0.5px;
  }
  .headline--on-time { left: 26px; top: 14px; color: var(--headline-red); }
  .headline--every-time { left: 86px; top: 99px; color: var(--headline-green); }
  .service-area-intro {
    position: absolute; left: 47px; top: 190px;
    color: var(--text-white);
    font-family: Arial, Helvetica, sans-serif;
    font-size: 20px;
  }
  .service-area {
    position: absolute; left: 50px; top: 221px;
    color: var(--accent-yellow);
    font-family: "Roboto", Arial, sans-serif;
    font-weight: 900; font-style: italic;
    font-size: 28px;
  }
  .client-mix { position: absolute; left: 576px; top: 26px; width: 372px; height: 108px; }
  .client-mix__text {
    position: absolute; left: 598px; top: 46px; width: 320px;
    color: var(--text-white);
    font-family: "Roboto", Arial, sans-serif;
    font-weight: 700; font-style: italic;
    font-size: 15px; line-height: 21px;
    text-align: center;
    transform: rotate(-3deg);
  }
  .promise {
    position: absolute; left: 500px; top: 155px; width: 245px;
    color: var(--text-white);
    font-size: 13.5px; line-height: 20px;
    text-align: center;
  }
  .promise .highlight { color: var(--accent-yellow); font-size: 16px; }
  .promise .hl { color: var(--accent-yellow); }
  .skyline {
    position: absolute; left: 332px; top: 250px;
    width: 660px; height: 174px;
    background: linear-gradient(to bottom, rgba(90,69,64,0) 0%, var(--skyline-top) 35%, var(--skyline-bottom) 100%);
  }
  .burst { position: absolute; left: 738px; top: 140px; width: 196px; height: 196px; }
  .burst__text {
    position: absolute; left: 758px; top: 177px; width: 150px;
    color: var(--text-black);
    font-family: "Roboto", Arial, sans-serif;
    font-weight: 700; font-style: italic;
    font-size: 15px; line-height: 21px;
    text-align: center;
    transform: rotate(-5deg);
  }
  .burst__text .weight { font-size: 46px; line-height: 46px; font-weight: 900; font-style: normal; }
  .burst__text .unit { font-size: 17px; }
  .courier-photo {
    position: absolute; left: 900px; top: 30px;
    width: 246px; height: 394px;
    background: linear-gradient(to bottom, #6b6e6c 0%, #545a58 40%, #b98f5f 55%, #a77d4d 75%, #3d5571 100%);
    border-radius: 60px 60px 0 0;
  }
  .profile {
    position: absolute; left: 116px; top: 533px;
    width: 243px; height: 243px;
    background: var(--profile-bg);
    display: flex; align-items: center; justify-content: center;
    text-align: center;
  }
  .profile__name {
    color: var(--brand-blue);
    font-family: "Roboto", Arial, sans-serif;
    font-weight: 700;
    font-size: 26px; line-height: 30px;
    padding: 0 20px;
  }
</style>
</head>
<body>
  <section class="cover" aria-label="Facebook cover">
    <h1 class="headline headline--on-time">On Time</h1>
    <p class="headline headline--every-time">Every Time</p>
    <p class="service-area-intro">We will only be delivering within</p>
    <p class="service-area">Yellowknife, NWT , Canada.</p>

    <div class="skyline" role="img" aria-label="City skyline silhouette"></div>

    <svg class="client-mix" viewBox="0 0 372 108" aria-hidden="true">
      <polygon points="30,22 372,0 344,84 0,106" fill="var(--headline-green)"/>
    </svg>
    <p class="client-mix__text">We aim to have 70 percent of our business from commercial clients and 30 percent from residential clients.</p>

    <p class="promise"><span class="highlight">We promise 100 % customer satisfaction</span> and offer our services <span class="hl">24 hours</span> a day <span class="hl">7 days</span> a week <span class="hl">365 days</span> a year .</p>

    <svg class="burst" viewBox="-98 -98 196 196" aria-hidden="true">
      <polygon fill="var(--accent-yellow)" points="95,0 78.5,15.6 87.8,36.4 66.5,44.5 67.2,67.2 44.5,66.5 36.4,87.8 15.6,78.5 0,95 -15.6,78.5 -36.4,87.8 -44.5,66.5 -67.2,67.2 -66.5,44.5 -87.8,36.4 -78.5,15.6 -95,0 -78.5,-15.6 -87.8,-36.4 -66.5,-44.5 -67.2,-67.2 -44.5,-66.5 -36.4,-87.8 -15.6,-78.5 0,-95 15.6,-78.5 36.4,-87.8 44.5,-66.5 67.2,-67.2 66.5,-44.5 87.8,-36.4 78.5,-15.6"/>
    </svg>
    <p class="burst__text">We will be<br>handling small<br>deliveries up to<br><span class="weight">20</span><span class="unit">pounds.</span></p>

    <div class="courier-photo" role="img" aria-label="Photo of a delivery courier carrying a cardboard parcel"></div>
  </section>

  <aside class="profile" aria-label="Profile picture">
    <p class="profile__name">Swift Lantern Courier &amp; Delivery Services</p>
  </aside>
</body>
</html>
```